My name is Tomas Berenji, and I have done business with your company several times. I need a business card to represent my business, I own a company by the name of VELMINO Suntan Lotion & Sunscreen.
My requirements are as follow: My company logo in the brightest gold possible, on a black, grainy (sandy) background, with shading around the each element. With the company name in gold, a stylized coconut trees, and some type of wave graphic in gold. "A product of the USA, Staten Island, NY"
"For comments, suggestion, or ordering please contact us at:
velmino42@brisalto.com"

"VELMINO™ Tanning Lotion & Sunscreen―Crafted with Care"

Velmino Tanning Lotion & Sunscreen is the most extraordinary and innovative sun tanning product to emerge in several generations. The constituents of this product are formidable substances that protect the skin against the aftermath of sun exposure−before you exposed yourself to the sun’s rays. The Aloe Vera in this product, along with other oils and cream, are specifically manufactured to lessen the symptoms of extended exposure to the sun. Velmino is designed to provide a Broad Spectrum Protection (50) that assist in the reduction of (UVA) and (UVB) radiation to create a magnificent sun-absorbing, long-lasting, deep dark bronzing experience.
Thank you,
Tomas Berenji
tomasbberenji@nexipost.com

Target Market(s)

Sunscreen

Industry/Entity Type

Business

Contact Information for Business Card

VELMINO™ Tanning Lotion and Sunscreen
Crafted with Care

Velmino Tanning Lotion is the most extraordinary and innovative sun tanning product to emerge in several generations. The constituents of this product are formidable substances that protect the skin against the aftermath of sun exposure−before you exposed yourself to the sun’s rays. The Aloe Vera, in this product, along with other oils and cream, are specifically manufactured to lessen the symptoms of extended exposure to the sun. Velmino protects your skin from dehydration and treat your skin with the products we apply to ourselves after a sunburn−before the sun tanning process begins. Velmino is designed to provide a Broad Spectrum Protection (50) that assist in the reduction of (UVA) and (UVB) radiation to create a magnificent sun-absorbing, long-lasting, deep dark bronzing experience.

Colors
fece3e
acd136

Requirements
Must have
• Black Card Stock with grainy surface, Gold Logo, stylized Coconut Palm Tree, Company Name, email address, and NYC location.
• Modern Layout with Modern fonts and graphics

```html
<!DOCTYPE html>
<html lang="en">
<head>
<meta charset="utf-8">
<title>VELMINO Business Card</title>
<link rel="stylesheet" href="https://fonts.googleapis.com/css2?family=Montserrat:wght@400;600;700&display=swap">
<style>
  :root {
    --backdrop: #d6d6d6;
    --card-black: #050505;
    --gold-bright: #fece3e;
    --gold-light: #fff3c4;
    --gold-mid: #d9a21f;
    --gold-deep: #9a6a12;
    --bronze: #5a2c14;
    --text-light: #f2f2f2;
  }
  * { margin: 0; padding: 0; box-sizing: border-box; }
  html, body {
    width: 1200px; height: 900px; overflow: hidden;
    background: var(--backdrop);
    font-family: "Montserrat", sans-serif;
  }
  .canvas { position: relative; width: 1200px; height: 900px; }
  .card {
    position: absolute;
    width: 620px; height: 354px;
    background: var(--card-black);
    border-radius: 26px;
    overflow: hidden;
    box-shadow: 0 14px 28px rgba(0,0,0,0.28);
  }
  .card--front { left: 90px; top: 60px; }
  .card--back { left: 490px; top: 480px; }

  .card__band { position: absolute; left: 0; bottom: 0; width: 100%; height: 16px; }
  .card__swoosh { position: absolute; left: 0; top: 0; width: 100%; height: 100%; }

  .brand {
    position: absolute;
    display: flex; flex-direction: column; align-items: center;
  }
  .card--front .brand { left: 50%; top: 92px; transform: translateX(-50%); }
  .card--back .brand { left: 70px; top: 96px; }
  .brand__dot {
    width: 72px; height: 72px; border-radius: 50%;
    background: var(--gold-mid);
    margin-bottom: 14px;
  }
  .brand__name {
    font-weight: 700; font-size: 46px; letter-spacing: 2px;
    color: var(--text-light);
  }
  .brand__name sup { font-size: 13px; font-weight: 700; vertical-align: 26px; margin-left: 2px; }

  .contact {
    position: absolute; left: 360px; top: 52px;
    color: var(--text-light);
  }
  .contact__name { font-weight: 700; font-size: 24px; color: var(--gold-bright); }
  .contact__role { font-size: 11px; letter-spacing: 1px; margin-top: 2px; }
  .contact__address { font-size: 11px; letter-spacing: 1px; line-height: 1.5; margin-top: 18px; }
  .contact__list { list-style: none; margin-top: 14px; font-size: 11px; letter-spacing: 1px; }
  .contact__list li { display: flex; align-items: center; gap: 10px; line-height: 1.9; }
  .contact__icon { width: 11px; height: 11px; flex: none; }
</style>
</head>
<body>
<main class="canvas">
  <!-- Front -->
  <section class="card card--front">
    <div class="brand">
      <div class="brand__dot"></div>
      <div class="brand__name">VELMINO<sup>TM</sup></div>
    </div>
    <svg class="card__band" viewBox="0 0 620 16" preserveAspectRatio="none" aria-hidden="true">
      <defs>
        <linearGradient id="bandGold" x1="0" x2="1" y1="0" y2="0">
          <stop offset="0" stop-color="var(--gold-deep)"/>
          <stop offset="0.2" stop-color="var(--gold-light)"/>
          <stop offset="0.55" stop-color="var(--gold-mid)"/>
          <stop offset="1" stop-color="var(--bronze)"/>
        </linearGradient>
      </defs>
      <rect x="0" y="0" width="620" height="16" fill="url(#bandGold)"/>
    </svg>
  </section>

  <!-- Back -->
  <section class="card card--back">
    <svg class="card__swoosh" viewBox="0 0 620 354" preserveAspectRatio="none" aria-hidden="true">
      <defs>
        <linearGradient id="swooshGold" x1="0" x2="1" y1="0" y2="0">
          <stop offset="0" stop-color="var(--gold-mid)"/>
          <stop offset="0.25" stop-color="var(--gold-light)"/>
          <stop offset="0.55" stop-color="var(--gold-mid)"/>
          <stop offset="0.85" stop-color="var(--gold-deep)"/>
          <stop offset="1" stop-color="var(--bronze)"/>
        </linearGradient>
        <linearGradient id="swooshBronze" x1="0" x2="1" y1="0" y2="1">
          <stop offset="0" stop-color="var(--gold-deep)"/>
          <stop offset="1" stop-color="var(--bronze)"/>
        </linearGradient>
      </defs>
      <path d="M0 300 C 220 290, 420 240, 620 110 L 620 354 L 0 354 Z" fill="url(#swooshGold)"/>
      <path d="M0 322 C 240 312, 440 262, 620 140 L 620 354 L 0 354 Z" fill="url(#swooshBronze)"/>
    </svg>

    <div class="brand">
      <div class="brand__dot"></div>
      <div class="brand__name">VELMINO<sup>TM</sup></div>
    </div>

    <div class="contact">
      <div class="contact__name">Tomas Berenji</div>
      <div class="contact__role">Manager</div>
      <div class="contact__address">Harbor View Complex<br>Staten Island, NY 10301</div>
      <ul class="contact__list">
        <li>
          <svg class="contact__icon" viewBox="0 0 12 12"><rect x="3" y="0.5" width="6" height="11" rx="1" fill="none" stroke="var(--gold-bright)" stroke-width="1.4"/></svg>
          555 0142 377
        </li>
        <li>
          <svg class="contact__icon" viewBox="0 0 12 12"><rect x="0.7" y="2" width="10.6" height="8" fill="none" stroke="var(--gold-bright)" stroke-width="1.4"/><path d="M1 2.5 L6 7 L11 2.5" fill="none" stroke="var(--gold-bright)" stroke-width="1.4"/></svg>
          velmino42@brisalto.com
        </li>
        <li>
          <svg class="contact__icon" viewBox="0 0 12 12"><circle cx="6" cy="6" r="5.3" fill="none" stroke="var(--gold-bright)" stroke-width="1.4"/><path d="M0.7 6 H11.3 M6 0.7 C3 4 3 8 6 11.3 M6 0.7 C9 4 9 8 6 11.3" fill="none" stroke="var(--gold-bright)" stroke-width="1"/></svg>
          www.velmino.com
        </li>
      </ul>
    </div>
  </section>
</main>
</body>
</html>
```